brightmesh Business Card

Already have the logo, but now need the business card design

Industry/Entity Type

Business Software

Contact Information for Business Card

web site will be brightmesh.io / The card should have the person name / position / mobile / email / and company address

Colors

Designer to choose colors to be used in the design.

Requirements
Must have
• See business card details
• One side to have the brightmesh logo
Nice to have
• If possible the 'O' from flow can be watermarked into the second side
• Try to fit in the words brightmesh Business Solutions

```html
<!DOCTYPE html>
<html lang="en">
<head>
<meta charset="utf-8">
<title>brightmesh Business Card</title>
<link href="https://fonts.googleapis.com/css2?family=Open+Sans:wght@300;400;600&display=swap" rel="stylesheet">
<style>
  :root {
    --stage: #2a2a2b;
    --brand-red: #e02a20;
    --card-grey: #4a4a4c;
    --ink-dark: #3b3b3d;
    --ink-light: #f1f1f1;
    --ink-soft: #cfcfd1;
  }
  * { box-sizing: border-box; margin: 0; padding: 0; }
  html, body {
    width: 800px;
    height: 1200px;
    overflow: hidden;
    background: var(--stage);
    font-family: "Open Sans", sans-serif;
  }
  .canvas {
    position: relative;
    width: 800px;
    height: 1200px;
  }
  .card {
    position: absolute;
    left: 80px;
    width: 640px;
    height: 366px;
    box-shadow: 0 18px 40px rgba(0, 0, 0, 0.45);
  }
  .card-front {
    top: 110px;
    background: var(--brand-red);
    display: flex;
    align-items: center;
    justify-content: center;
  }
  .front-wordmark {
    font-weight: 300;
    font-size: 72px;
    letter-spacing: -1px;
    color: var(--ink-dark);
  }
  .card-back {
    top: 660px;
    background: var(--card-grey);
    padding: 34px 40px;
    color: var(--ink-light);
  }
  .back-wordmark {
    font-weight: 300;
    font-size: 38px;
    line-height: 1;
    letter-spacing: -0.5px;
    color: var(--ink-light);
  }
  .tagline {
    margin-top: 4px;
    font-size: 10px;
    font-weight: 600;
    letter-spacing: 1.6px;
    color: var(--brand-red);
  }
  .person {
    margin-top: 30px;
  }
  .person-name {
    font-size: 15px;
    font-weight: 600;
    color: var(--brand-red);
  }
  .person-role {
    font-size: 11px;
    color: var(--ink-soft);
  }
  .address {
    margin-top: 16px;
    font-size: 11px;
    line-height: 1.5;
    color: var(--ink-soft);
  }
  .contacts {
    margin-top: 16px;
    list-style: none;
    font-size: 11px;
    color: var(--ink-soft);
  }
  .contacts li {
    display: flex;
    align-items: center;
    gap: 8px;
    line-height: 1.75;
  }
  .contacts svg {
    width: 11px;
    height: 11px;
    fill: var(--brand-red);
    flex: none;
  }
</style>
</head>
<body>
<main class="canvas">
  <section class="card card-front" aria-label="Business card front">
    <span class="front-wordmark">brightmesh</span>
  </section>

  <section class="card card-back" aria-label="Business card back">
    <div class="back-wordmark">brightmesh</div>
    <div class="tagline">BUSINESS SOLUTIONS</div>

    <div class="person">
      <div class="person-name">Marcus Ellery</div>
      <div class="person-role">Administrator</div>
    </div>

    <div class="address">
      1234 Any Street, Any Town,<br>
      Any City, Country 0000
    </div>

    <ul class="contacts">
      <li>
        <svg viewBox="0 0 24 24" aria-hidden="true"><path d="M6.6 10.8a15.1 15.1 0 0 0 6.6 6.6l2.2-2.2a1 1 0 0 1 1-.25 11.4 11.4 0 0 0 3.6.57 1 1 0 0 1 1 1V20a1 1 0 0 1-1 1A17 17 0 0 1 3 4a1 1 0 0 1 1-1h3.5a1 1 0 0 1 1 1c0 1.25.2 2.45.57 3.6a1 1 0 0 1-.25 1z"/></svg>
        555-014-2290
      </li>
      <li>
        <svg viewBox="0 0 24 24" aria-hidden="true"><path d="M2 5h20v14H2z M4 7v.4l8 5.2 8-5.2V7z" fill-rule="evenodd"/></svg>
        admin@brightmesh.io
      </li>
      <li>
        <svg viewBox="0 0 24 24" aria-hidden="true"><circle cx="12" cy="12" r="10"/></svg>
        www.brightmesh.io
      </li>
    </ul>
  </section>
</main>
</body>
</html>
```